QWR Consulting Web Design… We need a Facelift!

We currently have a website but it is very outdated. We like our content, but could use some help on giving it a refreshed facelift.

www.QWR-Consulting.example is our site

We only consult with large companies in the US that have sales over $250,000 a year, so looking to be high end yet approachable in our look.

Target Market(s)

Large corporations

Industry/Entity Type

Consulting

Coding

Coded - Design and coding required

Number of Pages Required

5+ page

Font styles to use
Serif
Sans Serif

Requirements
Must have
• We love our logo, keep that the same.
• The site colors can deviate from the logo, as long as it is complimentary
Nice to have
• We like our videos and graphics. If you can make them better, then great! But you can also feel free to reuse them.
• There is a video on the opening screen and one on the video page.
• We would like the video on the video page to be incorporated on the first page.
• If you think we need other/more page, we are all ears!
Should not have
• Want to set us apart from our competition in look, feel, professionalism and step away from the old fashioned conservatives of their websites. We want to be professional, yet bolder and fresher.
• Our Competition is LedgerBrook.example and TheHallowayPartners.example, but not looking to copy of emulate them, but gives an idea of the world QWR is in.

```html
<!DOCTYPE html>
<html lang="en">
<head>
<meta charset="utf-8">
<title>QWR Consulting</title>
<link rel="stylesheet" href="https://fonts.googleapis.com/css2?family=Open+Sans:wght@400;600;700;800&family=Lato:wght@400;700&display=swap">
<style>
:root{
  --red:#a51c1f;
  --red-dark:#8a1114;
  --ink:#333333;
  --muted:#555555;
  --blue-band:#8fb8f4;
  --blue-tile:#cfe0fb;
  --blue-pale:#eef3fc;
  --grey-bg:#f2f2f2;
  --footer:#585858;
  --footer-panel:#6b6b6b;
  --white:#ffffff;
}
*{box-sizing:border-box;margin:0;padding:0}
html,body{width:1200px;height:2679px;overflow:hidden}
body{position:relative;background:var(--white);font-family:"Lato",Arial,sans-serif;color:var(--ink)}
.abs{position:absolute}

/* header */
.site-header{position:absolute;left:0;top:0;width:1200px;height:143px;background:linear-gradient(#f7f7f7,#e4e4e4)}
.brand{position:absolute;left:0;top:0;width:388px;height:143px;background:var(--white);border-radius:0 0 90px 0;box-shadow:2px 0 6px rgba(0,0,0,.12)}
.brand-mark{position:absolute;left:140px;top:30px;display:flex;align-items:center;gap:14px}
.brand-dot{width:46px;height:46px;border-radius:50%;border:5px solid var(--red)}
.brand-name{font-family:"Open Sans",sans-serif;font-weight:700;font-size:40px;color:var(--ink);letter-spacing:4px}
.brand-url{position:absolute;left:140px;top:96px;font-family:"Open Sans",sans-serif;font-weight:700;font-size:19px;color:var(--muted)}
.contact-item{position:absolute;top:26px;display:flex;gap:12px;align-items:center}
.contact-item .label{font-size:15px;color:#5a86c9}
.contact-item .value{font-size:16px;font-weight:700;color:var(--ink)}
.main-nav{position:absolute;top:106px;left:0;width:1200px;font-family:"Open Sans",sans-serif;font-weight:700;font-size:14.5px;color:var(--ink)}
.main-nav a{position:absolute;color:inherit;text-decoration:none}
.main-nav a.active{color:var(--red)}

/* hero */
.hero{position:absolute;left:0;top:143px;width:1200px;height:327px;background:linear-gradient(90deg,#6e5642 0%,#8a6f58 45%,#a58d78 75%,#8a7462 100%)}
.hero-title{position:absolute;left:134px;top:140px;width:560px;text-align:center;font-family:"Open Sans",sans-serif;font-size:28px;color:var(--white);line-height:40px;letter-spacing:.3px}
.hero-dots{position:absolute;left:130px;top:293px;display:flex;gap:7px}
.hero-dots span{width:13px;height:13px;border-radius:50%;border:2px solid var(--red)}
.hero-dots span.on{background:var(--white);border-color:#ccc}

/* section heads */
.section-title{position:absolute;left:0;width:1200px;text-align:center;font-family:"Open Sans",sans-serif;font-weight:700;font-size:28px;color:var(--ink)}
.section-title em{font-style:normal;color:var(--red)}
.rule{position:absolute;height:2px;background:linear-gradient(90deg,transparent,#c9c9c9 20%,#c9c9c9 80%,transparent)}
.rule-knot{position:absolute;width:12px;height:12px;border-radius:50%;border:2px solid #8fa9d6;background:var(--white)}

/* process */
.step-icon{position:absolute;width:146px;height:146px;border-radius:50%;background:#3a3a3a;border:7px solid var(--red);box-shadow:0 12px 14px -8px rgba(0,0,0,.35);display:flex;align-items:center;justify-content:center}
.step-name{position:absolute;width:280px;text-align:center;font-family:"Open Sans",sans-serif;font-weight:700;font-size:18px;top:765px}
.step-list{position:absolute;width:300px;text-align:center;font-size:13.5px;line-height:24px;color:var(--muted);top:798px}
.dots{position:absolute;top:660px;display:flex;align-items:center;gap:14px}
.dots span{border-radius:50%;background:#e3e3e3}

/* welcome */
.welcome{position:absolute;left:0;top:902px;width:1200px;height:325px;background:var(--blue-pale)}
.welcome-head{position:absolute;left:134px;top:45px;display:flex;align-items:center;gap:14px;font-family:"Open Sans",sans-serif;font-weight:700;font-size:25px}
.welcome-head .dot{width:34px;height:34px;border-radius:50%;border:4px solid var(--red)}
.welcome-head .site{font-weight:600;color:#444}
.welcome-rule{position:absolute;left:134px;top:95px;width:590px;height:1px;background:#cfd6e2}
.welcome-text{position:absolute;left:134px;top:113px;width:590px;font-size:17.5px;line-height:27px;color:#444;text-align:justify;letter-spacing:.3px}
.video{position:absolute;left:764px;top:48px;width:298px;height:234px;background:var(--white);box-shadow:0 4px 14px rgba(0,0,0,.18);padding:10px}
.video-frame{position:relative;width:278px;height:214px;background:linear-gradient(90deg,#b9c3cc,#dfe5ea 55%,#9aa7b3)}
.video-play{position:absolute;left:118px;top:58px;width:48px;height:48px;border-radius:50%;background:rgba(255,255,255,.85);display:flex;align-items:center;justify-content:center}
.video-bar{position:absolute;left:0;bottom:0;width:278px;height:30px;background:#1d1d1d;display:flex;align-items:center;gap:10px;padding:0 10px;color:#fff;font-size:11px}
.video-track{flex:1;height:6px;border-radius:3px;background:#666;position:relative}
.video-track i{position:absolute;left:45%;top:-4px;width:14px;height:14px;border-radius:50%;background:#ddd}

/* why */
.why{position:absolute;left:0;top:1227px;width:1200px;height:252px;background:var(--blue-band)}
.why-tile{position:absolute;top:111px;width:150px;height:93px;background:var(--blue-tile);display:flex;flex-direction:column;align-items:center;justify-content:flex-end;padding-bottom:10px;gap:8px;font-family:"Open Sans",sans-serif;font-weight:700;font-size:14.5px;color:#222;box-shadow:0 1px 3px rgba(0,0,0,.15)}

/* topics */
.topic{position:absolute;width:232px;height:232px;border-radius:50%;overflow:hidden;box-shadow:0 3px 8px rgba(0,0,0,.2)}
.topic .photo{position:absolute;inset:0}
.topic .caption{position:absolute;left:0;bottom:0;width:232px;height:96px;background:linear-gradient(#b02a2a,#8e1417);color:var(--white);font-family:"Open Sans",sans-serif;font-weight:700;font-size:17px;line-height:21px;text-align:center;padding-top:16px}

/* testimonials */
.testimonials{position:absolute;left:0;top:2075px;width:1200px;height:330px;background:var(--grey-bg);border-top:4px solid #444}
.testimonials-tab{position:absolute;left:432px;top:-4px;width:336px;height:38px;background:#4a4a4a;clip-path:polygon(0 0,100% 0,94% 100%,6% 100%);color:var(--white);font-family:"Open Sans",sans-serif;font-weight:700;font-size:25px;text-align:center;line-height:36px}
.avatar{position:absolute;width:94px;height:94px;border-radius:50%;border:3px solid var(--red);background:linear-gradient(#c9c3bd,#8e8a86);box-shadow:0 14px 10px -10px rgba(0,0,0,.3)}
.quote{position:absolute;width:350px;font-size:14.5px;line-height:22.5px;color:#333}
.quote .mark{font-family:Georgia,serif;font-size:30px;color:#bbb;line-height:0}
.stars{position:absolute;color:#7ea3e4;font-size:17px;letter-spacing:1px}
.person{position:absolute;font-size:14px;color:#333}
.slider-rule{position:absolute;left:134px;top:273px;width:934px;height:1px;background:#bdbdbd}
.slider-btn{position:absolute;top:258px;width:30px;height:30px;border-radius:50%;display:flex;align-items:center;justify-content:center}

/* footer */
.site-footer{position:absolute;left:0;top:2405px;width:1200px;height:274px;background:var(--footer);color:var(--white)}
.inquiry{position:absolute;left:130px;top:0;width:281px;height:274px;background:var(--footer-panel)}
.footer-title{position:absolute;font-family:"Open Sans",sans-serif;font-weight:700;font-size:15px;color:var(--white)}
.field{position:absolute;background:var(--white);color:#555;font-size:11px;padding:5px 10px}
.btn{position:absolute;background:var(--red);color:var(--white);font-family:"Open Sans",sans-serif;font-weight:700;font-size:14px;border-radius:16px;text-align:center}
.social{position:absolute;top:2482px;width:40px;height:40px;border-radius:50%}
.info{position:absolute;display:flex;gap:10px;align-items:flex-start;font-size:12px;line-height:17px;color:#eee}
.footer-brand{position:absolute;left:905px;top:2546px;text-align:center;color:#ddd}
.footer-brand .row{display:flex;align-items:center;gap:8px;justify-content:center;font-family:"Open Sans",sans-serif;font-weight:700;font-size:24px}
.footer-brand .row i{width:22px;height:22px;border-radius:50%;border:3px solid #ddd}
.footer-brand .url{font-size:12px;margin-top:4px}
.copyright{position:absolute;left:411px;top:2646px;width:789px;text-align:center;font-size:12px;color:#eee}
</style>
</head>
<body>

<header class="site-header">
  <div class="brand">
    <div class="brand-mark"><span class="brand-dot"></span><span class="brand-name">QWR</span></div>
    <div class="brand-url">QWR-Consulting.example</div>
  </div>
  <div class="contact-item" style="left:643px">
    <svg width="32" height="32" viewBox="0 0 32 32"><path d="M9 4l5 6-3 3c1 3 4 6 7 8l3-3 6 5-3 4C14 27 5 18 4 8z" fill="none" stroke="#a51c1f" stroke-width="2.5"/></svg>
    <div><div class="label">Call Us:</div><div class="value">555-014-7890</div></div>
  </div>
  <div class="contact-item" style="left:821px">
    <svg width="40" height="32" viewBox="0 0 40 32"><rect x="3" y="6" width="32" height="22" fill="none" stroke="#a51c1f" stroke-width="2.5" transform="rotate(-10 19 17)"/><path d="M5 8l16 12 14-15" fill="none" stroke="#a51c1f" stroke-width="2.5"/></svg>
    <div><div class="label">Mail Us:</div><div class="value">Info@QWR-Consulting.example</div></div>
  </div>
  <nav class="main-nav">
    <a class="active" style="left:411px">HOME</a>
    <a style="left:479px">ABOUT US</a>
    <a style="left:573px">WHY QWR?</a>
    <a style="left:677px">SERVICES</a>
    <a style="left:768px">TESTIMONIALS</a>
    <a style="left:893px">CLIENTS</a>
    <a style="left:975px">CONTACT US</a>
  </nav>
</header>

<section class="hero" role="img" aria-label="Overhead photo of a team meeting around a white table on a wooden floor">
  <h1 class="hero-title">TAKING YOUR TREASURY PRICING PROCESS<br>TO UNPRECEDENTED LEVELS</h1>
  <div class="hero-dots"><span></span><span class="on"></span><span></span><span></span></div>
</section>

<!-- process -->
<h2 class="section-title" style="top:505px">OUR <em>PROCESS</em></h2>
<div class="rule" style="left:390px;top:556px;width:420px"></div>
<div class="rule-knot" style="left:608px;top:551px"></div>

<div class="step-icon" style="left:184px;top:597px">
  <svg width="70" height="70" viewBox="0 0 70 70"><path d="M35 8a27 27 0 0 1 25 18" fill="none" stroke="#fff" stroke-width="6"/><path d="M58 44a27 27 0 0 1-40 15" fill="none" stroke="#fff" stroke-width="6"/><path d="M12 48A27 27 0 0 1 20 13" fill="none" stroke="#fff" stroke-width="6"/><circle cx="35" cy="35" r="9" fill="#fff"/><circle cx="35" cy="8" r="6" fill="#fff"/><circle cx="60" cy="46" r="6" fill="#fff"/><circle cx="12" cy="48" r="6" fill="#fff"/></svg>
</div>
<div class="step-icon" style="left:531px;top:597px">
  <svg width="70" height="70" viewBox="0 0 70 70"><g fill="#fff"><circle cx="28" cy="28" r="16"/><rect x="24" y="6" width="8" height="44"/><rect x="6" y="24" width="44" height="8"/><rect x="24" y="6" width="8" height="44" transform="rotate(45 28 28)"/><rect x="24" y="6" width="8" height="44" transform="rotate(-45 28 28)"/><circle cx="50" cy="50" r="9"/><rect x="47" y="37" width="6" height="26"/><rect x="37" y="47" width="26" height="6"/></g><circle cx="28" cy="28" r="6" fill="#3a3a3a"/><circle cx="50" cy="50" r="3.5" fill="#3a3a3a"/></svg>
</div>
<div class="step-icon" style="left:868px;top:597px">
  <svg width="80" height="60" viewBox="0 0 80 60"><path d="M4 20l14-8 10 4 12-4 12 6 14-6 10 8-8 18-10 6-6 6-8-2-8 4-6-4-8-2-10-10z" fill="#fff"/><path d="M28 22l12 10 10-4M34 38l6 6M42 34l6 6" fill="none" stroke="#3a3a3a" stroke-width="2.5"/></svg>
</div>
<div class="dots" style="left:367px"><span style="width:12px;height:12px"></span><span style="width:16px;height:16px"></span><span style="width:20px;height:20px"></span><span style="width:28px;height:28px"></span></div>
<div class="dots" style="left:714px"><span style="width:12px;height:12px"></span><span style="width:16px;height:16px"></span><span style="width:20px;height:20px"></span><span style="width:28px;height:28px"></span></div>

<div class="step-name" style="left:117px">MODEL</div>
<div class="step-list" style="left:107px">Gather statements<br>Bullet Analyze against market<br>Bullet Calculate profitability</div>
<div class="step-name" style="left:464px">ENGAGE</div>
<div class="step-list" style="left:454px">Review win-win strategies<br>Bullet Discuss with providers<br>Bullet Finalize agreements</div>
<div class="step-name" style="left:801px">AUDIT</div>
<div class="step-list" style="left:791px">Inspect pricing adherence<br>Bullet Continue market benchmarking<br>Bullet Complete contract compliance</div>

<!-- welcome -->
<section class="welcome">
  <div class="welcome-head">WELCOME TO <span class="dot"></span><span class="site">QWR-Consulting.example</span></div>
  <div class="welcome-rule"></div>
  <p class="welcome-text">We are a consortium of ex-bankers, consultants, certified treasury professionals, and former practitioners that combined our resources with the objective of participating in a common activity for achieving a common goal: assisting clients in maximizing the return of their treasury and cash management relationships by uncovering details that typically only bankers know.</p>
  <div class="video">
    <div class="video-frame" role="img" aria-label="Video still of a smiling consultant in an office with colleagues behind">
      <div class="video-play"><svg width="20" height="22" viewBox="0 0 20 22"><path d="M3 2l15 9-15 9z" fill="#666"/></svg></div>
      <div class="video-bar">
        <svg width="10" height="12" viewBox="0 0 10 12"><path d="M0 0l10 6-10 6z" fill="#fff"/></svg>
        <span>04:59</span><div class="video-track"><i></i></div><span>10:35</span>
        <svg width="14" height="12" viewBox="0 0 14 12"><path d="M0 4h3l4-4v12l-4-4H0z" fill="#fff"/><path d="M9 3q3 3 0 6" stroke="#fff" fill="none"/></svg>
      </div>
    </div>
  </div>
</section>

<!-- why -->
<section class="why">
  <h2 class="section-title" style="top:36px">WHY <em>QWR?</em></h2>
  <div class="rule" style="left:390px;top:81px;width:420px;background:linear-gradient(90deg,transparent,#dce8fc 20%,#dce8fc 80%,transparent)"></div>
  <div class="rule-knot" style="left:608px;top:76px;background:var(--blue-band);border-color:#fff"></div>

  <div class="why-tile" style="left:150px">
    <svg width="44" height="40" viewBox="0 0 44 40"><g fill="#a51c1f"><rect x="4" y="28" width="6" height="10"/><rect x="13" y="22" width="6" height="16"/><rect x="22" y="24" width="6" height="14"/><rect x="31" y="16" width="6" height="22"/></g><path d="M3 22l12-10 8 6 14-14" stroke="#a51c1f" stroke-width="3" fill="none"/><path d="M32 2h8v8z" fill="#a51c1f"/></svg>PROFITABILITY</div>
  <div class="why-tile" style="left:337px">
    <svg width="44" height="40" viewBox="0 0 44 40"><g fill="#a51c1f"><path d="M22 2l20 9H2z"/><rect x="3" y="12" width="38" height="3"/><rect x="6" y="17" width="5" height="16"/><rect x="15" y="17" width="5" height="16"/><rect x="24" y="17" width="5" height="16"/><rect x="33" y="17" width="5" height="16"/><rect x="2" y="34" width="40" height="4"/></g></svg>INSIDERS</div>
  <div class="why-tile" style="left:525px">
    <svg width="52" height="40" viewBox="0 0 80 60"><path d="M4 20l14-8 10 4 12-4 12 6 14-6 10 8-8 18-10 6-6 6-8-2-8 4-6-4-8-2-10-10z" fill="#a51c1f"/><path d="M28 22l12 10 10-4M34 38l6 6M42 34l6 6" fill="none" stroke="#cfe0fb" stroke-width="2.5"/></svg>INVOLVED</div>
  <div class="why-tile" style="left:712px">
    <svg width="40" height="40" viewBox="0 0 40 40"><rect x="6" y="2" width="26" height="34" fill="none" stroke="#a51c1f" stroke-width="3"/><path d="M11 10h16M11 16h16M11 22h10" stroke="#a51c1f" stroke-width="2.5"/><path d="M22 30l5 5 10-10" stroke="#a51c1f" stroke-width="3" fill="none"/></svg>THOROUGH</div>
  <div class="why-tile" style="left:900px">
    <svg width="40" height="40" viewBox="0 0 40 40"><circle cx="22" cy="16" r="12" fill="none" stroke="#a51c1f" stroke-width="3.5"/><path d="M13 25L3 36" stroke="#a51c1f" stroke-width="5"/><circle cx="22" cy="16" r="5" fill="#a51c1f"/></svg>DATA</div>
</section>

<!-- topics -->
<div class="topic" style="left:154px;top:1529px"><div class="photo" role="img" aria-label="Hands reviewing printed financial charts" style="background:linear-gradient(135deg,#e9eef6,#c7d3e4 60%,#d8a08a)"></div><div class="caption">KNOW THE<br>MARKET</div></div>
<div class="topic" style="left:484px;top:1529px"><div class="photo" role="img" aria-label="Road rising into a blue sky with an upward arrow" style="background:linear-gradient(#6f9fd6,#cfe2f5 45%,#8fae57 70%,#5c7a34)"></div><div class="caption">UNDERSTAND<br>PROFITABILITY</div></div>
<div class="topic" style="left:813px;top:1529px"><div class="photo" role="img" aria-label="Team of business people stacking hands together" style="background:linear-gradient(135deg,#dcdcdc,#6b6b6b 55%,#2e2e2e)"></div><div class="caption">AUGMENT YOUR<br>TEAM</div></div>
<div class="topic" style="left:320px;top:1793px"><div class="photo" role="img" aria-label="Calculator, pen and bank statement on a desk" style="background:linear-gradient(135deg,#f2f2f2,#b8b8b8 60%,#8c8c8c)"></div><div class="caption">WHAT BANKS<br>WANT</div></div>
<div class="topic" style="left:648px;top:1793px"><div class="photo" role="img" aria-label="Hand typing on a laptop keyboard" style="background:linear-gradient(135deg,#4a4a4a,#a08a78 55%,#d9c6b4)"></div><div class="caption">AVOID SWITCHING<br>PROVIDERS</div></div>

<!-- testimonials -->
<section class="testimonials">
  <div class="testimonials-tab">CLIENT TESTIMONIALS</div>
  <div class="avatar" role="img" aria-label="Portrait of a client" style="left:133px;top:76px"></div>
  <p class="quote" style="left:240px;top:80px"><span class="mark">&ldquo;</span> Duis autem vel eum iriure dolor in hendrerit in vulputate velitj esse molestie consequat, vel illum dolore eu feugiat nulla facilis sis at vero eros et accumsan et delenit facilisi. <span class="mark">&rdquo;</span></p>
  <div class="stars" style="left:240px;top:175px">★★★★★</div>
  <div class="person" style="left:240px;top:202px">Mr. Alan Brevik</div>

  <div class="avatar" role="img" aria-label="Portrait of a client" style="left:624px;top:76px"></div>
  <p class="quote" style="left:732px;top:80px"><span class="mark">&ldquo;</span> Duis autem vel eum iriure dolor in hendrerit in vulputate velitj esse molestie consequat, vel illum dolore eu feugiat nulla facilis sis at vero eros et accumsan et delenit facilisi. <span class="mark">&rdquo;</span></p>
  <div class="stars" style="left:736px;top:175px">★★★★★</div>
  <div class="person" style="left:740px;top:202px">Miss Nora Brevik</div>

  <div class="slider-rule"></div>
  <div class="slider-btn" style="left:578px;background:#cfcfcf"><svg width="10" height="14" viewBox="0 0 10 14"><path d="M8 1L2 7l6 6" stroke="#fff" stroke-width="2.5" fill="none"/></svg></div>
  <div class="slider-btn" style="left:614px;background:#333"><svg width="10" height="14" viewBox="0 0 10 14"><path d="M2 1l6 6-6 6" stroke="#fff" stroke-width="2.5" fill="none"/></svg></div>
</section>

<!-- footer -->
<footer class="site-footer">
  <div class="inquiry">
    <div class="footer-title" style="left:20px;top:22px">QUICK INQUIRY</div>
    <div class="field" style="left:20px;top:58px;width:243px;height:27px">Name</div>
    <div class="field" style="left:20px;top:96px;width:243px;height:27px">Email</div>
    <div class="field" style="left:20px;top:134px;width:243px;height:75px">Message</div>
    <div class="btn" style="left:20px;top:222px;width:102px;height:32px;line-height:32px">SUBMIT</div>
  </div>
  <div class="footer-title" style="left:461px;top:22px">NEWSLETTER SIGNUP</div>
  <div class="field" style="left:461px;top:58px;width:268px;height:36px;font-size:12px;padding-top:10px">Enter Your Email</div>
  <div class="btn" style="left:739px;top:60px;width:91px;height:32px;line-height:32px">SUBMIT</div>
  <div class="abs" style="left:861px;top:20px;width:1px;height:235px;background:#777"></div>
  <div class="abs" style="left:461px;top:122px;width:390px;height:1px;background:#6c6c6c"></div>
  <div class="footer-title" style="left:902px;top:22px">SOCIAL CONNECT</div>
</footer>
<div class="social" style="left:900px;background:#3b5ea8"></div>
<div class="social" style="left:950px;background:#d8493a"></div>
<div class="social" style="left:998px;background:#33a8e8"></div>

<div class="info" style="left:462px;top:2548px;width:180px">
  <svg width="14" height="20" viewBox="0 0 14 20"><path d="M7 0a7 7 0 0 1 7 7c0 5-7 13-7 13S0 12 0 7a7 7 0 0 1 7-7z" fill="#fff"/><circle cx="7" cy="7" r="2.5" fill="#585858"/></svg>
  <span>GB12 Fusce mollis antdipi<br>ullamcrper vestibulu<br>misiacus 123-456</span>
</div>
<div class="info" style="left:660px;top:2550px;font-size:19px;line-height:22px;color:#fff">
  <svg width="12" height="20" viewBox="0 0 12 20"><rect x="1" y="1" width="10" height="18" rx="2" fill="#fff"/><rect x="3" y="4" width="6" height="10" fill="#585858"/></svg>
  <span>555-014-7890</span>
</div>
<div class="info" style="left:660px;top:2592px;font-size:13px">
  <svg width="14" height="12" viewBox="0 0 14 12"><rect x="0" y="1" width="14" height="10" fill="#fff"/><path d="M0 1l7 6 7-6" stroke="#585858" fill="none"/></svg>
  <span>Info@QWR-Consulting.example</span>
</div>
<div class="footer-brand">
  <div class="row"><i></i>QWR</div>
  <div class="url">QWR-Consulting.example</div>
</div>
<div class="copyright">© 2016 QWR-Consulting.example. All Rights Reserved.</div>

</body>
</html>
```